business card with logo Velmora Nails & Spa 2816 SW Quillan Ave Portland OR 97384

Would like to have a business card with our logo.
like bottle of polish with our logo or letter V on it
want something that first glance would let you know that it is a nail salon.
like the hands with polish bottle dripping.
like black or White back ground

Velmora Nails & Spa
(The Velvet Retreat)
2816 SW Quillan Ave
Portland, OR 97384
Call or Text: 1-503-555-0148
www.VelmoraNailsnSpa.example
Open 7 days a week.
After 7:00 PM is by appointment only.
Closed only on Thanksgiving & Christmas.

Target Market(s)

20%Man and 80%Woman 13-70

Industry/Entity Type

Business

Contact Information for Business Card

Elegant with Logo-Business name- address-phone-open days. closed day.

Font styles to use
Decorative
Script

Colors
000000

Requirements
Must have
• Logo and place for Technician Name
• Velmora Nails & Spa
• (The Velvet Retreat)
• 2816 SW Quillan Ave
• Portland, OR 97384
• Call or Text: 1-503-555-0148
• Open 7 days a week
• Closed only on Thanksgiving & Christmas.
• We accepted all major credit cards but prefer cash. Thank you
Nice to have
• Nail polish bottle with our Logo or letter V
Should not have
• too colorful

```html
<!DOCTYPE html>
<html lang="en">
<head>
<meta charset="utf-8">
<title>Velmora Nails &amp; Spa – Business Card</title>
<link rel="stylesheet" href="https://fonts.googleapis.com/css2?family=Great+Vibes&family=Ubuntu:wght@400;500;700&display=swap">
<style>
  :root {
    --page-bg: #e4e2df;
    --card-top: #f7f7f6;
    --card-bottom: #ecebea;
    --ink: #1b1b1b;
    --ink-soft: #4a4a4a;
    --accent-red: #d5141d;
    --art-light: #e2dfdc;
    --art-dark: #bdb8b4;
    --band: #060606;
    --band-text: #ffffff;
  }
  * { margin: 0; padding: 0; box-sizing: border-box; }
  html, body {
    width: 1200px;
    height: 900px;
    overflow: hidden;
    background: var(--page-bg);
  }
  .business-card {
    position: absolute;
    left: 120px;
    top: 155px;
    width: 960px;
    height: 590px;
    border-radius: 26px;
    overflow: hidden;
    background: linear-gradient(180deg, var(--card-top), var(--card-bottom));
    box-shadow: 0 18px 40px rgba(0, 0, 0, 0.18);
    font-family: "Ubuntu", sans-serif;
    color: var(--ink);
  }
  .technician-name {
    position: absolute;
    left: 64px;
    top: 68px;
    font-family: "Great Vibes", cursive;
    font-size: 46px;
    line-height: 1;
    color: var(--accent-red);
  }
  .technician-title {
    position: absolute;
    left: 76px;
    top: 132px;
    font-size: 24px;
  }
  .contact-phone {
    position: absolute;
    left: 74px;
    top: 172px;
    font-size: 24px;
  }
  .contact-phone .label {
    color: var(--accent-red);
    font-weight: 500;
  }
  .logo-art {
    position: absolute;
    border-radius: 14px;
    background: linear-gradient(135deg, var(--art-light), var(--art-dark));
    opacity: 0.75;
  }
  .logo-art--hand {
    left: 665px;
    top: 58px;
    width: 230px;
    height: 66px;
  }
  .logo-art--foot {
    left: 480px;
    top: 236px;
    width: 96px;
    height: 82px;
  }
  .brand-name {
    position: absolute;
    left: 480px;
    top: 136px;
    width: 440px;
    text-align: center;
    font-size: 44px;
    line-height: 1.1;
    font-weight: 400;
    letter-spacing: 0.5px;
    color: var(--ink);
  }
  .brand-tagline {
    position: absolute;
    left: 600px;
    top: 200px;
    width: 320px;
    text-align: center;
    font-size: 22px;
    color: var(--ink-soft);
  }
  .policy-notes {
    position: absolute;
    left: 60px;
    top: 294px;
    font-size: 24px;
    line-height: 35px;
  }
  .hours-info {
    position: absolute;
    right: 54px;
    top: 340px;
    text-align: right;
    font-size: 24px;
    line-height: 35px;
  }
  .hours-info .website {
    color: var(--accent-red);
  }
  .address-band {
    position: absolute;
    left: 0;
    bottom: 0;
    width: 100%;
    height: 112px;
    background: var(--band);
    color: var(--band-text);
    display: flex;
    align-items: center;
    justify-content: center;
    font-size: 26px;
    word-spacing: 2px;
  }
</style>
</head>
<body>
  <section class="business-card">
    <p class="technician-name">Marcus Ellery</p>
    <p class="technician-title">Managing Director</p>
    <p class="contact-phone"><span class="label">Call or Text:</span> 1-503-555-0148</p>

    <div class="logo-art logo-art--hand" role="img" aria-label="Line illustration of a hand with red painted nails"></div>
    <div class="logo-art logo-art--foot" role="img" aria-label="Line illustration of a foot with a red painted toenail"></div>
    <p class="brand-name">Velmora Nails &amp; Spa</p>
    <p class="brand-tagline">(The Velvet Retreat)</p>

    <p class="policy-notes">
      Closed only on Thanksgiving<br>
      &amp; Christmas.<br>
      We accepted all major credit<br>
      cards but prefer cash. Thank you
    </p>

    <p class="hours-info">
      Open 7 days a week.<br>
      After 7:00 PM is by appointment only.<br>
      <span class="website">www.VelmoraNailsnSpa.example</span>
    </p>

    <footer class="address-band">2816 SW Quillan Ave&nbsp; Portland, OR 97384</footer>
  </section>
</body>
</html>
```